1 page marketing brochure for subcontractor services for Florida's Petroleum Contamination cleanup

I need a marketing brochure that can be emailed to potential clients to offer our comprehensive service capabilities to Agency Term Contractors in the Coastal Bureau of Habitat Stewardship's (CBHS) Fuel Recovery Initiative. We offer turnkey support from project management, monitoring, reporting, soil and groundwater assessment, remediation system engineering, design, construction, and system rental. We would like to see designs that use the green and goldish colors in our logo. I have attached the icon from our logo and an amateur in-house created design with some key points that are important to us. The icons used as bullet points can change. I've added examples of industry correct drilling icons. I also added a second picture of a system trailer in use. We are open to different Fonts and are open to assistance with copy refinement. This single page flyer is intended only for digital use (email/website) at this time.
Updates

Target Market(s)

Agency Term contractors in Coastal Bureau of Habitat Stewardship Fuel Recovery Initiative

Industry/Entity Type

Petroleum cleanup in Florida

Requirements
Should not have
• Don't show the Varnel name in the photo. See attached examples of industry appropriate drilling icons

```html
<!DOCTYPE html>
<html lang="en">
<head>
<meta charset="utf-8">
<title>Palmetta Construction – Subcontractor Services</title>
<link rel="stylesheet" href="https://fonts.googleapis.com/css2?family=Manrope:wght@500;600;700&display=swap">
<style>
  :root{
    --green:#12562f;
    --green-deep:#0f4d2a;
    --gold:#c9b57a;
    --gold-dark:#b9a665;
    --sage:#dfe9d8;
    --white:#ffffff;
    --sky:#5d8fd0;
    --cloud:#e9eef5;
    --ground:#cfcac2;
    --tree:#2f4d2a;
  }
  *{margin:0;padding:0;box-sizing:border-box}
  html,body{width:1200px;height:1200px;overflow:hidden;background:var(--white)}
  .flyer{position:relative;width:1200px;height:1200px;overflow:hidden;font-family:"Manrope",sans-serif}
  .backdrop{position:absolute;inset:0}
  .brand{position:absolute;left:103px;top:104px;display:flex;align-items:center;gap:22px}
  .brand-square{width:86px;height:86px;background:var(--green)}
  .brand-name{color:var(--green);font-weight:600;font-size:35px;line-height:1.15}
  .photo{position:absolute;overflow:hidden}
  .photo-site{left:755px;top:0;width:445px;height:472px;border-radius:0 0 48% 52% / 0 0 34% 56%;
    background:linear-gradient(180deg,var(--sky) 0%,var(--cloud) 35%,var(--tree) 45%,#6f8f4c 52%,var(--ground) 60%,#bdb6ab 100%)}
  .photo-trailer{left:728px;top:800px;width:385px;height:345px;border-radius:48% 52% 40% 46% / 30% 36% 40% 50%;
    background:linear-gradient(180deg,var(--sky) 0%,var(--cloud) 22%,var(--tree) 32%,#e6e6e4 45%,#bfbfbd 80%,#d8d6d2 100%)}
  .copy{position:absolute;left:103px;color:var(--white)}
  .headline{top:338px;font-weight:700;font-size:40px;line-height:50px;letter-spacing:-.2px}
  .subhead{top:514px;font-weight:700;font-size:40px;line-height:50px}
  .intro{top:578px;font-weight:500;font-size:21px;line-height:32px;width:650px}
  .services{position:absolute;left:103px;top:706px;list-style:none;color:var(--white);font-weight:500;font-size:22px;line-height:35px}
  .services li{position:relative;padding-left:62px}
  .services .icon{position:absolute;left:0;top:2px;width:38px;height:38px}
  .s1{margin-bottom:12px}.s2{margin-bottom:12px}.s3{margin-bottom:20px}.s4{margin-bottom:22px}.s5{margin-bottom:6px}
</style>
</head>
<body>
<main class="flyer">
  <svg class="backdrop" width="1200" height="1200" viewBox="0 0 1200 1200" aria-hidden="true">
    <rect width="1200" height="1200" fill="var(--gold)"/>
    <path d="M1200 420 C1120 470 1090 520 1040 470 L1000 1200 L1200 1200 Z" fill="var(--gold-dark)" opacity=".5"/>
    <path d="M640 0 H780 C760 120 720 200 660 230 Z" fill="var(--sage)"/>
    <path d="M0 0 H760 C720 150 640 255 520 262 L130 266 C70 268 30 285 0 310 Z" fill="var(--white)"/>
    <path d="M0 310 C40 280 80 268 130 266 L520 262 C620 258 690 330 770 430 C830 505 850 580 880 640 C910 700 1000 720 1040 770 L1060 900 C1000 1000 820 1100 600 1200 L0 1200 Z" fill="var(--green)"/>
  </svg>

  <div class="brand">
    <span class="brand-square"></span>
    <span class="brand-name">Palmetta<br>Construction</span>
  </div>

  <div class="photo photo-site" role="img" aria-label="Photo of a white remediation system trailer parked on a cleared site under a blue sky"></div>

  <h1 class="copy headline">Comprehensive<br>Capabilities for<br>Subcontracted Projects</h1>
  <h2 class="copy subhead">Agency Term Contractors</h2>
  <p class="copy intro">Project management, monitoring and reporting for the Coastal Bureau of Habitat Stewardship (CBHS) Fuel Recovery Initiative</p>

  <ul class="services">
    <li class="s1">
      <svg class="icon" viewBox="0 0 38 38"><path d="M9 9 L26 19 L9 29 Z" fill="var(--gold)"/></svg>
      Turnkey support for Agency Term Contractors,<br>statewide
    </li>
    <li class="s2">
      <svg class="icon" viewBox="0 0 38 38"><circle cx="19" cy="19" r="17" fill="none" stroke="var(--gold)" stroke-width="2.5"/><path d="M11 19 L17 25 L27 13" fill="none" stroke="var(--gold)" stroke-width="3" stroke-linecap="round" stroke-linejoin="round"/></svg>
      Project management, monitoring, reporting<br>Soil and groundwater assessment,
    </li>
    <li class="s3">
      <svg class="icon" viewBox="0 0 38 38" fill="none" stroke="var(--gold)" stroke-width="3" stroke-linecap="round"><path d="M6 6 H32 M19 6 V32 M10 32 H28 M6 22 H32"/></svg>
      Remediation engineering, design, construction<br>System rental
    </li>
    <li class="s4">
      <svg class="icon" viewBox="0 0 38 38"><path d="M9 9 L26 19 L9 29 Z" fill="var(--gold)"/></svg>
      Trusted partner for every phase:
    </li>
    <li class="s5">
      <svg class="icon" viewBox="0 0 38 38" fill="none" stroke="var(--gold)" stroke-width="2.5"><circle cx="19" cy="19" r="17"/><path d="M19 8 V30 M13 30 H25" stroke-linecap="round"/></svg>
      Portable remediation systems serving<br>all of Florida
    </li>
    <li>
      <svg class="icon" viewBox="0 0 38 38" fill="none" stroke="var(--gold)" stroke-width="2.5"><circle cx="19" cy="19" r="17"/><path d="M12 19 L17 24 L26 14" stroke-linecap="round" stroke-linejoin="round"/></svg>
      Proven regulatory compliance
    </li>
  </ul>

  <div class="photo photo-trailer" role="img" aria-label="Photo of an enclosed remediation system trailer with hose reels, shown in use on site"></div>
</main>
</body>
</html>
```